Whitcombe Framing Works - Card Design

I am looking to use the logo designs that you already did for me to develop a business card. I would like the card to have a black background and be double sided. I want white and green logo and text. I have attached an inspiration photo of a look that I like. I would like to use the Vertical Logo attached to take up the full front side of the card. On the back where I have my name and information, I would like to have the horizontal logo or maybe even just the image of the 'A' and trees without the text. I am open, but I am looking for something clean and simple and I want the green to really pop! Additional files can be found under Design #: 40593216

Target Market(s)

Homeowners

Industry/Entity Type

Construction

Contact Information for Business Card

Name: Marcus Pellow, Title: Project Manager, Phone: 555.555.0147, Email: whitcombeframingworks@mailbarn.net, address: 418 Juniper Ln, Cedar Hollow, CA 95092, Lic# 2046318

Colors
00AB8E
00BBA5
67D7C9
C6EFE9
E9F9F6

Requirements
Nice to have
• I would like to see the logos that I have already got from SketchHarbor, though I am open to new ones

```html
<!DOCTYPE html>
<html lang="en">
<head>
<meta charset="utf-8">
<title>Whitcombe Framing Works – Business Card</title>
<link rel="stylesheet" href="https://fonts.googleapis.com/css2?family=Montserrat:wght@400;500;700&display=swap">
<style>
  :root {
    --backdrop: #1f1f21;
    --card: #2b2829;
    --card-light: #3a3637;
    --green: #2a9d3c;
    --green-bright: #35b84a;
    --white: #f4f4f4;
    --silver: #b9b9bb;
  }
  * { box-sizing: border-box; margin: 0; padding: 0; }
  html, body { width: 1200px; height: 1200px; overflow: hidden; }
  body {
    background: var(--backdrop);
    font-family: "Montserrat", sans-serif;
    position: relative;
  }
  .card {
    position: absolute;
    left: 220px;
    width: 760px;
    height: 434px;
    background: radial-gradient(ellipse at 50% 40%, var(--card-light), var(--card) 70%);
    box-shadow: 0 18px 40px rgba(0,0,0,0.55);
    overflow: hidden;
  }
  .card--front { top: 110px; }
  .card--back { top: 620px; }

  /* Front */
  .front-mark {
    position: absolute;
    left: 50%; top: 50%;
    transform: translate(-50%, -50%);
    display: flex;
    align-items: center;
    gap: 18px;
    white-space: nowrap;
  }
  .front-mark__circle {
    flex: 0 0 auto;
    width: 54px; height: 54px;
    border: 3px solid var(--silver);
    border-radius: 50%;
  }
  .front-mark__name {
    font-weight: 700;
    font-size: 30px;
    letter-spacing: 1px;
    color: var(--silver);
    text-transform: uppercase;
  }

  /* Back */
  .identity {
    position: absolute;
    left: 40px; top: 78px;
    width: 310px;
    text-align: right;
  }
  .brand {
    display: flex;
    justify-content: flex-end;
    align-items: center;
    gap: 10px;
    margin-bottom: 22px;
    white-space: nowrap;
  }
  .brand__circle {
    flex: 0 0 auto;
    width: 30px; height: 30px;
    border: 2px solid var(--white);
    border-radius: 50%;
  }
  .brand__name {
    font-weight: 700;
    font-size: 15px;
    color: var(--white);
    text-transform: uppercase;
    letter-spacing: 0.5px;
  }
  .person__name {
    font-weight: 700;
    font-size: 30px;
    color: var(--green-bright);
    line-height: 1.1;
    white-space: nowrap;
  }
  .person__title {
    margin-top: 8px;
    font-size: 16px;
    color: var(--white);
  }
  .divider {
    position: absolute;
    left: 372px; top: 70px;
    width: 2px; height: 200px;
    background: var(--green-bright);
  }
  .contact {
    position: absolute;
    left: 400px; top: 72px;
    color: var(--white);
    font-size: 22px;
    line-height: 1.3;
    white-space: nowrap;
  }
  .contact__address { margin-bottom: 20px; }
  .contact__phone { display: flex; align-items: center; gap: 10px; margin-bottom: 10px; }
  .contact__phone svg { width: 20px; height: 20px; }
  .band {
    position: absolute;
    left: 0; right: 0; bottom: 0;
    height: 92px;
    background: var(--green);
    display: flex;
    align-items: center;
    padding-left: 48px;
    gap: 14px;
    color: var(--white);
    font-size: 19px;
  }
  .band svg { width: 20px; height: 16px; }
</style>
</head>
<body>
  <section class="card card--front" aria-label="Card front">
    <div class="front-mark">
      <span class="front-mark__circle"></span>
      <span class="front-mark__name">Whitcombe Framing Works</span>
    </div>
  </section>

  <section class="card card--back" aria-label="Card back">
    <div class="identity">
      <div class="brand">
        <span class="brand__circle"></span>
        <span class="brand__name">Whitcombe Framing Works</span>
      </div>
      <p class="person__name">Marcus Pellow</p>
      <p class="person__title">Project Manager</p>
    </div>
    <div class="divider"></div>
    <div class="contact">
      <p class="contact__address">418 Juniper Ln, Cedar Hollow,<br>CA 95092</p>
      <p class="contact__phone">
        <svg viewBox="0 0 24 24" aria-hidden="true"><path fill="#35b84a" d="M6.6 10.8a15 15 0 0 0 6.6 6.6l2.2-2.2a1 1 0 0 1 1-.25 11.4 11.4 0 0 0 3.6.57 1 1 0 0 1 1 1V20a1 1 0 0 1-1 1A17 17 0 0 1 3 4a1 1 0 0 1 1-1h3.5a1 1 0 0 1 1 1c0 1.25.2 2.45.57 3.57a1 1 0 0 1-.25 1z"/></svg>
        555.555.0147
      </p>
      <p class="contact__license">Lic# 2046318</p>
    </div>
    <div class="band">
      <svg viewBox="0 0 20 16" aria-hidden="true"><rect x="0" y="0" width="20" height="16" fill="#f4f4f4"/><path d="M0 0l10 8 10-8" fill="none" stroke="#2a9d3c" stroke-width="2"/></svg>
      <span>whitcombeframingworks@mailbarn.net</span>
    </div>
  </section>
</body>
</html>
```